Accounting & Tax Services in Edmonton, Canada-Needs Website Design & Improvement

I am starting my business for accounting and tax services in Canada. I have my website but not much happy with that. My services are for bookkeeping, accounting and tax services. We serve both individual and corporate clients. I am trying to bring new idea in the market for providing services at their facility or business. My existing website is www.kvrm.ca
Currently, this site is static but I want to improve it to dynamic or interactive in nature.

Target Market(s)

Edmonton and Surrounding Areas, Canada

Industry/Entity Type

Public Accounting

Logo Text

Lakeshore Ledger & Office Partners

Number of Pages Required

4 page

Font styles to use
Sans Serif

Colors

Designer to choose colors to be used in the design.

Requirements
Must have
• 4 Pages
• I a not sure what do we mean by coded and uncoded design. Need clarification
• Rest is explained in project description. It should have the ingredients to attract traffic in any professional website.
• Logo Design Text can be shortened, if required.
• Existing logo attached, just for reference.
Nice to have
• 5 Pages

```html
<!DOCTYPE html>
<html lang="en">
<head>
<meta charset="utf-8">
<title>Lakeshore Ledger &amp; Office Partners</title>
<link rel="stylesheet" href="https://fonts.googleapis.com/css2?family=Montserrat:wght@400;500;600;700&family=Roboto+Slab:wght@300&family=PT+Sans+Narrow:wght@400;700&display=swap">
<style>
  :root {
    --teal: #157a78;
    --teal-glass: rgba(22, 128, 124, 0.78);
    --yellow: #f5bd2a;
    --white: #ffffff;
    --nav-glass: rgba(236, 242, 242, 0.82);
    --nav-text: #1f2a2c;
    --city-dark: #1e2b30;
    --city-mid: #3d5257;
    --city-warm: #7a6448;
  }
  * { box-sizing: border-box; margin: 0; padding: 0; }
  html, body { width: 1200px; height: 612px; overflow: hidden; background: var(--city-dark); }
  .page { position: relative; width: 1200px; height: 612px; overflow: hidden; font-family: "Montserrat", sans-serif; }

  .hero-photo {
    position: absolute; inset: 0;
    background:
      radial-gradient(ellipse at 35% 70%, rgba(122,100,72,0.55), transparent 45%),
      radial-gradient(ellipse at 85% 30%, rgba(122,100,72,0.4), transparent 40%),
      linear-gradient(160deg, var(--city-mid) 0%, var(--city-dark) 55%, #151f23 100%);
  }

  .site-header {
    position: absolute; left: 224px; top: 10px; width: 750px; height: 80px;
    background: var(--nav-glass); border-radius: 4px;
    display: flex; align-items: center;
  }
  .brand { display: flex; align-items: center; gap: 7px; margin-left: 18px; }
  .brand-dot { width: 16px; height: 16px; border-radius: 50%; background: var(--teal); }
  .brand-name { font-size: 10.5px; font-weight: 600; color: var(--teal); }
  .main-nav { position: absolute; left: 259px; top: 0; height: 80px; display: flex; }
  .main-nav a {
    display: flex; align-items: center; height: 80px; padding: 0 9px;
    font-size: 8.8px; font-weight: 600; color: var(--nav-text); text-decoration: none; letter-spacing: 0.1px;
  }
  .main-nav a.is-active { background: var(--yellow); color: var(--white); padding: 0 10px; }
  .social { position: absolute; left: 676px; top: 32px; display: flex; gap: 9px; }
  .social span { width: 14px; height: 14px; border-radius: 50%; background: var(--teal); }

  .welcome { position: absolute; left: 239px; top: 197px; color: var(--white); }
  .welcome-kicker { font-size: 9.5px; letter-spacing: 1.6px; font-weight: 500; }
  .welcome-title { margin-top: 21px; font-size: 28px; font-weight: 500; line-height: 34.5px; }
  .welcome-rule { margin-top: 20px; width: 62px; height: 2px; background: var(--yellow); }

  .intro-bubble { position: absolute; left: 673px; top: 186px; }
  .intro-bubble svg { position: absolute; left: 0; top: 0; }
  .intro-content { position: relative; padding: 30px 22px 0 24px; width: 261px; color: var(--white); }
  .quote-mark { font-size: 64px; font-weight: 700; line-height: 40px; height: 34px; margin-left: 10px; letter-spacing: -4px; }
  .intro-text { margin-top: 22px; font-family: "Roboto Slab", serif; font-weight: 300; font-size: 9.6px; line-height: 15px; }
  .btn-more {
    display: inline-block; margin: 15px 0 0 7px; width: 125px; height: 25px; line-height: 25px; text-align: center;
    background: var(--yellow); color: var(--white); font-size: 8.8px; font-weight: 600; text-decoration: none;
  }

  .notice {
    position: absolute; left: 151px; top: 443px; width: 943px; height: 125px;
    background: var(--teal); color: var(--white); text-align: center; font-family: "PT Sans Narrow", sans-serif;
  }
  .notice-line { margin-top: 22px; font-size: 22px; letter-spacing: 0.1px; }
  .notice-url { margin-top: 2px; font-size: 38px; font-weight: 700; font-family: "Montserrat", sans-serif; letter-spacing: -0.5px; }
</style>
</head>
<body>
<div class="page">
  <div class="hero-photo" role="img" aria-label="Aerial photograph of a downtown skyline of glass office towers at dusk"></div>

  <header class="site-header">
    <div class="brand"><span class="brand-dot"></span><span class="brand-name">Lakeshore Ledger &amp; Office Partners</span></div>
    <nav class="main-nav">
      <a class="is-active" href="#">HOME</a>
      <a href="#">PROFILE</a>
      <a href="#">SERVICES</a>
      <a href="#">NEWS</a>
      <a href="#">TOOLS</a>
      <a href="#">INFO CENTER</a>
      <a href="#">CONTACT</a>
    </nav>
    <div class="social" aria-label="Social links"><span></span><span></span><span></span></div>
  </header>

  <section class="welcome">
    <p class="welcome-kicker">WELCOME TO</p>
    <h1 class="welcome-title">Lakeshore Ledger<br>&amp; Office<br>Partners</h1>
    <div class="welcome-rule"></div>
  </section>

  <aside class="intro-bubble">
    <svg width="262" height="256" viewBox="0 0 262 256" aria-hidden="true">
      <path d="M24 0 H238 Q262 0 262 24 V185 Q262 209 238 209 H60 L0 256 V24 Q0 0 24 0 Z" fill="var(--teal-glass)"/>
    </svg>
    <div class="intro-content">
      <div class="quote-mark">"</div>
      <p class="intro-text">Welcome and thank you for visiting our website. At Lakeshore Ledger &amp; Office Partners, we have built our business so that it guarantees your success.</p>
      <a class="btn-more" href="#">MORE ABOUT US</a>
    </div>
  </aside>

  <section class="notice">
    <p class="notice-line">PLEASE VISIT THE ONLINE WORDPRESS VERSION OF THE WEBSITE ON THE FOLLOWING LINK:</p>
    <p class="notice-url">www.northgate-webworks.net/lakeshoreledger</p>
  </section>
</div>
</body>
</html>
```